Redesign two student school awards

I need to redesign 2 students awards. I need the elements of the letterhead to be incorporated into the Student Awards. I have covered some of the letterhead elements to show just the 4 elements that need to be incorporated: school emblem, school name, "For so much, what shall we repay?", and the 3 coloured ribbon. The awards need to be in colour and the use of the 3 school colours - purple, yellow (gold) and chocolate brown,

I have upload the 2 awards the school presents to students (they are printed on A4 Paper). The first one is the:

(1) Year Adviser Award - this award needs to include the school name; the title: Year Adviser's Award; Award to; Name (where the word is deleted and the office staff type the students name or uploaded names which can be autofilled); for the following achievements; the year (which can be changed an include the day and month (but auto filled); Year Adviser (where the teacher signs their name - see lower left of the award; (also the 5 categories - School Service, Community Service , Sporting Achievements, Leadership, Academic Achievement (these 5 categories must be able to be deleted as a student may receive the Year Adviser's Award for 1 or 2 of the categories)

(2) Principal's Award - all elements of this award need to be included. In this example there's a fake name Dale Foster - this is where the office staff type in the students name or hopefully upload a list of names that are auto filled. The 5 categories need to be retained e.g. School Service, Community Service etc (these can be fixed as they are not deleted; for the following achievements; the year (which can be changed an include the day and month (but auto filled); my name and title,

For the 2 student awards it would be good if the design is in a computer program where the office staff can auto fill students names.

The main goal is to redesign the 2 awards, whilst retaining current elements and include 4 of the elements from the letter head.

Target Market(s)

School students (12 years old to 18 years old)

Industry/Entity Type

Education

Font styles to use
Serif

Requirements
Must have
• The elements and school colours mentioned in the description. Would be helpful if the computer program it is contained in allows for auto fill of student names, date, and for the Year Advisers award any one of the five award categories can be removed. To be printed on A4 paper/card

Colours must contain the school colours as mentioned before and the 4 elements of the letterhead. I am trying to have all our communications and awards contain similar elements.

```html
<!DOCTYPE html>
<html lang="en">
<head>
<meta charset="utf-8">
<title>Principal's Award – Glen Ridge Memorial High School</title>
<link rel="stylesheet" href="https://fonts.googleapis.com/css2?family=Noto+Serif:ital,wght@0,700;1,700&family=Roboto:ital,wght@0,400;0,700;1,400&display=swap">
<style>
  :root {
    --purple: #94418f;
    --gold: #e8e322;
    --brown: #3a1a22;
    --paper: #f1f1f1;
    --band-grey: #e2e2e5;
    --ink: #111111;
    --backdrop: #c25fbb;
  }
  * { margin: 0; padding: 0; box-sizing: border-box; }
  html, body {
    width: 1135px; height: 1200px; overflow: hidden;
    background: var(--backdrop);
  }
  .award {
    position: absolute; left: 167px; top: 28px;
    width: 800px; height: 1144px;
    background: var(--paper);
    overflow: hidden;
    color: var(--ink);
  }
  .award__header-band {
    position: absolute; left: 0; top: 20px; width: 100%; height: 88px;
    background: linear-gradient(180deg, var(--gold) 0%, var(--purple) 45%, var(--brown) 100%);
    opacity: 0.9;
  }
  .award__school {
    position: absolute; top: 126px; left: 0; width: 100%;
    text-align: center;
    font: italic 700 29px/1 "Noto Serif", serif;
    letter-spacing: 0.5px;
  }
  .award__title {
    position: absolute; top: 165px; left: 0; width: 100%;
    text-align: center;
    font: 400 23px/1 "Roboto", sans-serif;
    letter-spacing: 1px;
  }
  .emblem {
    position: absolute; left: 249px; top: 222px; width: 303px; height: 270px;
    display: flex; flex-direction: column; align-items: center; justify-content: center; gap: 18px;
  }
  .emblem__disc {
    width: 160px; height: 160px; border-radius: 50%;
    background: var(--purple);
  }
  .emblem__name {
    font: italic 700 28px/1 "Noto Serif", serif;
    color: var(--brown);
  }
  .awarded-to {
    position: absolute; top: 515px; left: 88px; width: 624px; height: 40px;
    display: flex; align-items: center; gap: 14px;
    font: 400 34px/1 "Roboto", sans-serif;
  }
  .awarded-to__arrow { flex: 1; height: 24px; }
  .name-band {
    position: absolute; top: 576px; left: 0; width: 100%; height: 111px;
    background: var(--band-grey);
    display: flex; align-items: center; justify-content: center;
  }
  .name-band__name {
    font: italic 700 70px/1 "Noto Serif", serif;
    letter-spacing: 1px;
  }
  .rule-brown {
    position: absolute; top: 687px; left: 0; width: 100%; height: 8px; background: var(--brown);
  }
  .achievements-band {
    position: absolute; top: 695px; left: 0; width: 100%; height: 36px;
    background: var(--gold);
    display: flex; align-items: center; justify-content: center;
    font: italic 400 22px/1 "Roboto", sans-serif; letter-spacing: 1.5px;
    color: var(--brown);
  }
  .achievements {
    position: absolute; top: 731px; left: 0; width: 800px; height: 270px;
    background: var(--brown);
  }
  .achievements__list {
    position: absolute; top: 22px; left: 0; width: 100%;
    list-style: none; text-align: center;
    font: italic 700 29px/42px "Noto Serif", serif;
    letter-spacing: 1px;
    color: var(--paper);
  }
  .signature {
    position: absolute; left: 42px; top: 1032px;
  }
  .signature__role {
    font: italic 400 23px/1 "Roboto", sans-serif; color: var(--brown); letter-spacing: 0.5px;
  }
  .signature__name {
    margin-top: 8px;
    font: 700 27px/1 "Noto Serif", serif;
  }
  .award__year {
    position: absolute; left: 667px; top: 1067px; width: 83px; height: 31px;
    background: var(--gold);
    display: flex; align-items: center; justify-content: center;
    font: 700 23px/1 "Roboto", sans-serif; letter-spacing: 2px;
  }
</style>
</head>
<body>
<main class="award">
  <div class="award__header-band" role="img" aria-label="School colours ribbon banner in gold, purple and brown"></div>

  <h1 class="award__school">GLEN RIDGE MEMORIAL HIGH SCHOOL</h1>
  <p class="award__title">Principal’s Award</p>

  <div class="emblem">
    <div class="emblem__disc"></div>
    <span class="emblem__name">Glen Ridge High</span>
  </div>

  <div class="awarded-to">
    <svg class="awarded-to__arrow" viewBox="0 0 200 24" preserveAspectRatio="none" aria-hidden="true">
      <path d="M4,12 H200 M14,2 L4,12 L14,22 M22,2 L12,12 L22,22" fill="none" stroke="var(--ink)" stroke-width="2"/>
    </svg>
    <span>Awarded to</span>
    <svg class="awarded-to__arrow" viewBox="0 0 200 24" preserveAspectRatio="none" aria-hidden="true">
      <path d="M0,12 H196 M186,2 L196,12 L186,22 M178,2 L188,12 L178,22" fill="none" stroke="var(--ink)" stroke-width="2"/>
    </svg>
  </div>

  <div class="name-band"><span class="name-band__name">Dale Foster</span></div>
  <div class="rule-brown"></div>
  <div class="achievements-band">for the following achievements</div>

  <section class="achievements">
    <ul class="achievements__list">
      <li>School Service</li>
      <li>Community Service</li>
      <li>Sporting Achievement</li>
      <li>Leadership</li>
      <li>Academic Achievement</li>
    </ul>
  </section>

  <div class="signature">
    <p class="signature__role">Principal:</p>
    <p class="signature__name">Mr K. Ellison</p>
  </div>
  <div class="award__year">2020</div>
</main>
</body>
</html>
```